Sproutlab 3.0 - Educational Guide/Course-pack/Worksheet

Our Sproutlab 3.0 toolkit is an educational workshop that focuses on inspiring student initiatives in the classroom! We need a new educational course guide or course-pack for students/teachers that clearly outlines or explains the program steps, offers helpful tips and includes empty spaces/lines where their can write down their great ideas or notes. This will include a;

- Teachers Guide (1 Page)
- Student Guide/Worksheet (4 Pages)
- Group Pack Resources (3 Pages)

This will consist of designing/formatting text, stock animation/icons, font, etc. We have included our new logo (color, branding, etc.) and all of the text for each separate course-pack. We have also attached our new website to give you an idea of the program style.

Our workshop can be for any school project like Technology, Community, Environment, Art, Science, etc.

Target Market(s)

High School Students/Teachers

Industry/Entity Type

Education

Font styles to use
Sans Serif

Colors
f68e4e
acd037
34a7d8

Requirements
Must have
• Use our brand colors from logo.
Should not have
• Should not be too childish.

```html
<!DOCTYPE html>
<html lang="en">
<head>
<meta charset="UTF-8">
<title>Sproutlab 3.0 – Who Does What?</title>
<link href="https://fonts.googleapis.com/css2?family=Roboto+Condensed:wght@300;400;700&display=swap" rel="stylesheet">
<style>
  :root {
    --brand-orange: #f58e4e;
    --brand-green: #acd037;
    --brand-blue: #34a7d8;
    --ink: #000000;
    --paper: #ffffff;
  }
  * { margin: 0; padding: 0; box-sizing: border-box; }
  html, body { width: 927px; height: 1200px; overflow: hidden; background: var(--paper); }
  .page {
    position: relative;
    width: 927px;
    height: 1200px;
    border: 1px solid var(--ink);
    font-family: "Roboto Condensed", "Arial Narrow", sans-serif;
    color: var(--ink);
  }
  .brand {
    position: absolute;
    left: 46px;
    top: 72px;
    display: flex;
    align-items: center;
    gap: 14px;
  }
  .brand-mark {
    width: 40px;
    height: 40px;
    border-radius: 50%;
    background: var(--brand-blue);
    flex: none;
  }
  .brand-name {
    font-size: 32px;
    font-weight: 700;
    line-height: 1;
    color: var(--ink);
  }
  .sheet-title {
    position: absolute;
    left: 43px;
    top: 183px;
    font-size: 24px;
    font-weight: 700;
  }
  .intro {
    position: absolute;
    left: 104px;
    top: 224px;
    font-size: 17px;
    font-weight: 300;
    line-height: 22px;
  }
  .intro p + p { margin-top: 22px; }
  .task-table {
    position: absolute;
    left: 103px;
    top: 356px;
    width: 734px;
    border-collapse: collapse;
    table-layout: fixed;
  }
  .task-table th, .task-table td {
    border: 2px solid var(--ink);
    height: 35.3px;
  }
  .task-table th {
    background: var(--brand-orange);
    font-size: 18px;
    font-weight: 700;
    text-align: center;
  }
  .task-table tbody tr:nth-child(even) td { background: var(--brand-orange); }
  .col-task { width: 326px; }
  .col-who { width: 204px; }
</style>
</head>
<body>
<div class="page">
  <header class="brand">
    <span class="brand-mark"></span>
    <div class="brand-name">Sproutlab 3.0</div>
  </header>

  <h1 class="sheet-title">Who Does What?</h1>

  <div class="intro">
    <p>You can use the ‘Who Does What?’ in two ways.</p>
    <p>1. Make and update a list of all the things the whole group needs to do.<br>
    2. Each person in the group can use it to keep track of everything that needs to be done in their “committee”.<br>
    Ex. Marketing, fund-raising, or production.</p>
  </div>

  <table class="task-table">
    <colgroup><col class="col-task"><col class="col-who"><col></colgroup>
    <thead>
      <tr><th>Task</th><th>Who will do it?</th><th>When will you do it?</th></tr>
    </thead>
    <tbody>
      <tr><td></td><td></td><td></td></tr>
      <tr><td></td><td></td><td></td></tr>
      <tr><td></td><td></td><td></td></tr>
      <tr><td></td><td></td><td></td></tr>
      <tr><td></td><td></td><td></td></tr>
      <tr><td></td><td></td><td></td></tr>
      <tr><td></td><td></td><td></td></tr>
      <tr><td></td><td></td><td></td></tr>
      <tr><td></td><td></td><td></td></tr>
      <tr><td></td><td></td><td></td></tr>
      <tr><td></td><td></td><td></td></tr>
      <tr><td></td><td></td><td></td></tr>
      <tr><td></td><td></td><td></td></tr>
      <tr><td></td><td></td><td></td></tr>
      <tr><td></td><td></td><td></td></tr>
      <tr><td></td><td></td><td></td></tr>
      <tr><td></td><td></td><td></td></tr>
      <tr><td></td><td></td><td></td></tr>
      <tr><td></td><td></td><td></td></tr>
      <tr><td></td><td></td><td></td></tr>
      <tr><td></td><td></td><td></td></tr>
    </tbody>
  </table>
</div>
</body>
</html>
```